Ecommerce website Home Page Design that is clean and elegant

Design a Home page for an ecommerce website. This website products and offerings will be very similar to :

brightmeadowtrinkets.com
pebblelanegoods.com

Target Market(s)

Consumer and small shops who can order online.

Industry/Entity Type

Retail

Number of Pages Required

1 page

Colors

Designer to choose colors to be used in the design.

Requirements
Must have
• Exact competition with similar products:
• brightmeadowtrinkets.com
• http://www.pebblelanegoods.com/
• Home page with featured image banner
• List of items on sale or category based items list
• atleast three banners for sale or shipping related offers.
Nice to have
• The logo has very light colors and products will have lots of colors as you can see on competition sites. So the design must consider this so that logo also stands out somewhat for branding purpose.
Should not have
• Design should not have black background

```html
<!DOCTYPE html>
<html lang="en">
<head>
<meta charset="utf-8">
<title>Partyloom – Party Supplies &amp; Novelties</title>
<link rel="stylesheet" href="https://fonts.googleapis.com/css2?family=Open+Sans:wght@400;600;700&family=Raleway:wght@500;600;700;800&display=swap">
<style>
:root{
  --ink:#222;
  --text:#444;
  --muted:#888;
  --line:#dcdcdc;
  --topbar:#9a9a9a;
  --gold:#d8ad45;
  --teal:#4b8a96;
  --band:#7aa3ae;
  --white:#fff;
  --logo:#8a78b8;
}
*{box-sizing:border-box;margin:0;padding:0}
html,body{width:1200px;height:3109px;overflow:hidden}
body{position:relative;background:var(--white);font-family:"Open Sans",Arial,sans-serif;color:var(--text)}
.abs{position:absolute}
a{color:inherit;text-decoration:none}

/* top bar */
.topbar{left:0;top:0;width:1200px;height:29px;background:var(--topbar);color:#fff;font-size:11px;display:flex;align-items:center;padding:0 99px}
.topbar .right{margin-left:auto;display:flex;gap:26px}
.topbar span{display:inline-flex;align-items:center;gap:6px}

/* header */
.header{left:0;top:29px;width:1200px;height:89px}
.logo{left:99px;top:24px;display:flex;align-items:center;gap:10px;font-family:"Raleway",sans-serif;font-weight:700;font-size:38px;color:var(--logo)}
.logo .dot{width:14px;height:14px;border-radius:50%;background:var(--logo)}
.search{left:573px;top:28px;width:330px;height:30px;border-bottom:1px solid #bbb;font-size:10px;color:var(--muted);display:flex;align-items:center;justify-content:space-between;letter-spacing:.5px}
.cart{left:940px;top:22px;display:flex;gap:12px;font-size:12px;color:var(--ink)}
.cart small{display:block;font-size:10px;color:var(--muted);margin-top:3px}

/* nav */
.nav{left:0;top:118px;width:1200px;height:40px;border-top:1px solid var(--line);display:flex;align-items:center;justify-content:space-between;padding:0 107px;font-family:"Raleway",sans-serif;font-weight:700;font-size:13px;color:var(--ink);letter-spacing:.3px}

/* hero */
.hero{left:0;top:158px;width:1200px;height:445px;background:linear-gradient(100deg,#1f2228 0%,#3b3340 40%,#6a4a5a 62%,#2a2630 100%)}
.hero-photo{right:0;top:0;width:560px;height:445px;background:radial-gradient(circle at 45% 45%,#b99386 0%,#5b4650 45%,rgba(40,35,45,0) 75%)}
.hero h1{left:97px;top:138px;font-family:"Raleway",sans-serif;font-weight:800;font-size:48px;color:#fff;letter-spacing:.5px}
.hero p{left:99px;top:206px;font-size:20px;color:#fff}
.btn-gold{background:var(--gold);color:#fff;font-family:"Raleway",sans-serif;font-weight:700;font-size:12px;letter-spacing:.5px;display:flex;align-items:center;justify-content:center}
.hero .btn-gold{left:99px;top:255px;width:164px;height:38px;font-size:13px}
.arrow-btn{top:200px;width:34px;height:44px;background:rgba(0,0,0,.35);display:flex;align-items:center;justify-content:center}

/* promos */
.promo{top:613px;height:224px;color:#fff;padding:50px 28px}
.promo h3{font-family:"Raleway",sans-serif;font-weight:800;font-size:25px;letter-spacing:.5px}
.promo p{font-family:"Raleway",sans-serif;font-weight:700;font-size:17px;margin-top:8px}
.promo .shop{display:inline-block;margin-top:26px;border:2px solid #fff;padding:6px 12px;font-size:12px;font-weight:700;font-family:"Raleway",sans-serif}

/* section titles */
.section-title{left:0;width:1200px;text-align:center;font-family:"Raleway",sans-serif;font-weight:700;font-size:30px;color:var(--ink)}

/* categories */
.cat{display:flex;align-items:flex-end;padding:20px 16px;color:#fff;font-family:"Raleway",sans-serif;font-weight:800;font-size:18px;line-height:1.5}
.cat.big{padding:26px 28px;font-size:20px}

.divider{left:99px;top:1434px;width:1002px;height:1px;background:var(--line)}

/* products */
.product{width:228px}
.product .img{width:228px;height:238px;border:1px solid #cfcfcf}
.product .img div{position:absolute;inset:30px}
.product h4{font-weight:400;font-size:14px;color:var(--ink);line-height:25px;margin-top:26px;width:212px}
.product .price{color:var(--teal);font-size:14px;margin-top:6px}
.product .actions{display:flex;gap:5px;margin-top:12px}
.product .actions .btn-gold{width:110px;height:25px;font-size:11px}
.icon-btn{width:25px;height:25px;border:1px solid #c9c9c9;display:flex;align-items:center;justify-content:center;font-size:12px}

.view-more{left:0;top:2455px;width:1200px;text-align:center;font-family:"Raleway",sans-serif;font-weight:700;font-size:13px;color:#666}
.view-more span{border-bottom:1px solid #999;padding-bottom:2px}

/* features band */
.band{left:0;top:2560px;width:1200px;height:167px;background:var(--band);color:#fff}
.feature{top:58px;display:flex;align-items:center;gap:16px}
.feature b{display:block;font-family:"Raleway",sans-serif;font-size:19px;font-weight:700}
.feature small{display:block;font-size:12px;margin-top:3px}

/* footer */
.fcol{top:2805px;font-size:11px;color:#555}
.fcol h5{font-family:"Raleway",sans-serif;font-weight:700;font-size:17px;color:var(--ink);margin-bottom:18px}
.fcol li{list-style:none;line-height:29px}
.fsep{top:2800px;width:1px;height:200px;background:var(--line)}
.subscribe{display:flex;margin-top:22px}
.subscribe .input{width:230px;height:36px;border:1px solid #ccc;font-size:11px;padding:11px 12px;color:#666}
.subscribe .btn-gold{width:93px;height:36px;font-size:11px}
.social{display:flex;gap:9px;margin-top:14px}
.social i{width:32px;height:32px;border-radius:50%;background:var(--teal);display:block}
.copyright{left:0;top:3040px;width:1200px;border-top:1px solid var(--line);padding-top:22px;text-align:center;font-size:11px;color:#555}
</style>
</head>
<body>

<div class="abs topbar">
  <span>☎ 1 800 555 0142</span>&nbsp;&nbsp;|&nbsp;&nbsp;<span>✉ sales@partyloom.com</span>
  <div class="right">
    <span>Checkout</span><span>♥ Wishlist</span><span>My Account</span><span>Login</span><span>Register</span>
  </div>
</div>

<header class="abs header">
  <div class="abs logo"><span>Partyloom</span><span class="dot"></span></div>
  <div class="abs search"><span>SEARCH</span>
    <svg width="16" height="16" viewBox="0 0 16 16"><circle cx="6.5" cy="6.5" r="5" fill="none" stroke="#555" stroke-width="2"/><line x1="10" y1="10" x2="15" y2="15" stroke="#555" stroke-width="2"/></svg>
  </div>
  <div class="abs cart">
    <svg width="30" height="28" viewBox="0 0 30 28"><path d="M1 3h5l4 15h15l3-11H8" fill="none" stroke="#d8ad45" stroke-width="2.5"/><circle cx="12" cy="24" r="2.5" fill="#d8ad45"/><circle cx="23" cy="24" r="2.5" fill="#d8ad45"/></svg>
    <div>My Cart<small>0 item(s) | $0.00 ⌄</small></div>
  </div>
</header>

<nav class="abs nav">
  <a>PARTY SUPPLIES</a><a>DECORATIONS SUPPLIES</a><a>OCCASIONS &amp; EVENTS</a><a>TOYS &amp; GAMES</a><a>CRAFTS</a><a>HOLIDAYS</a>
</nav>

<section class="abs hero">
  <div class="abs hero-photo" role="img" aria-label="Woman wearing a black masquerade mask amid falling confetti"></div>
  <h1 class="abs">PARTY WEARABLES</h1>
  <p class="abs">At vero eos et accusamus etusto erty</p>
  <a class="abs btn-gold">GET MORE INFO</a>
  <div class="abs arrow-btn" style="left:0"><svg width="10" height="16"><path d="M8 1L2 8l6 7" fill="none" stroke="#fff" stroke-width="2"/></svg></div>
  <div class="abs arrow-btn" style="right:0"><svg width="10" height="16"><path d="M2 1l6 7-6 7" fill="none" stroke="#fff" stroke-width="2"/></svg></div>
</section>

<div class="abs promo" style="left:0;width:394px;background:linear-gradient(90deg,#c7addb,#d9c4e6)" role="img" aria-label="Child in sunglasses and sun hat, free shipping offer">
  <h3>FREE SHIPPING</h3><p>ON ORDER OVER $100</p><span class="shop">SHOP NOW!</span>
</div>
<div class="abs promo" style="left:404px;width:392px;background:linear-gradient(90deg,#8fcad0,#a9d6da)" role="img" aria-label="Party hats and gifts on a table, big sale offer">
  <h3>BIG SALE</h3><p>SAVE UP TO 50%</p><span class="shop">SHOP NOW!</span>
</div>
<div class="abs promo" style="left:806px;width:394px;background:linear-gradient(90deg,#e3a7bb,#f0c6cf)" role="img" aria-label="Summer hat and accessories, summer clearance offer">
  <h3>SUMMER CLEARANCE</h3><p>UP TO 75% OFF</p><span class="shop">SHOP NOW!</span>
</div>

<h2 class="abs section-title" style="top:910px">PRODUCTS CATEGORIES</h2>

<div class="abs cat big" style="left:99px;top:993px;width:500px;height:362px;background:linear-gradient(120deg,#9cc8c6,#b9d7c8 45%,#e3a3ae)" role="img" aria-label="Colourful streamers and party glasses on a wooden table">OCCASIONS &amp;<br>EVENTS</div>
<div class="abs cat" style="left:622px;top:993px;width:228px;height:170px;background:linear-gradient(135deg,#c8b76a,#7f8c5a)" role="img" aria-label="Children playing games in a playroom">TOYS &amp;<br>GAMES</div>
<div class="abs cat" style="left:870px;top:993px;width:230px;height:170px;background:linear-gradient(135deg,#6a4fa3,#d0508a 60%,#f0a24c)" role="img" aria-label="Bright balloons and party decorations">DECORATIONS &amp;<br>SUPPLIES</div>
<div class="abs cat" style="left:622px;top:1185px;width:228px;height:170px;background:linear-gradient(135deg,#e7b88f,#d67a6b)" role="img" aria-label="Happy children at a birthday party">PARTY<br>SUPPLIES</div>
<div class="abs cat" style="left:870px;top:1185px;width:230px;height:170px;background:radial-gradient(circle at 50% 40%,#3a5a2a,#050505 65%)" role="img" aria-label="Glowing neon glasses and light sticks">GLOW<br>PRODUCTS</div>

<div class="abs divider"></div>

<h2 class="abs section-title" style="top:1489px">FEATURED PRODUCTS</h2>

<div class="abs product" style="left:99px;top:1571px">
  <div class="img" style="position:relative"><div role="img" aria-label="Striped party hat with blower" style="background:radial-gradient(circle,#f1cf3c 0%,#e6703c 45%,#fff 72%)"></div></div>
  <h4>At vero eos et accusamus et iust odio dignissimos</h4><div class="price">$69.99</div>
  <div class="actions"><a class="btn-gold">ADD TO CART</a><span class="icon-btn">♥</span><span class="icon-btn">i</span><span class="icon-btn">⇄</span></div>
</div>
<div class="abs product" style="left:357px;top:1571px">
  <div class="img" style="position:relative"><div role="img" aria-label="Straw fedora hat with sunglasses" style="background:radial-gradient(circle,#d9c08e 0%,#c9a56a 40%,#fff 72%)"></div></div>
  <h4>At vero eos et accusamus et iust odio dignissimos</h4><div class="price">$69.99</div>
  <div class="actions"><a class="btn-gold">ADD TO CART</a><span class="icon-btn">♥</span><span class="icon-btn">i</span><span class="icon-btn">⇄</span></div>
</div>
<div class="abs product" style="left:615px;top:1571px">
  <div class="img" style="position:relative"><div role="img" aria-label="Stack of colourful fidget spinners" style="background:radial-gradient(circle,#5cc05a 0%,#e24f3c 40%,#fff 72%)"></div></div>
  <h4>At vero eos et accusamus et iust odio dignissimos</h4><div class="price">$69.99</div>
  <div class="actions"><a class="btn-gold">ADD TO CART</a><span class="icon-btn">♥</span><span class="icon-btn">i</span><span class="icon-btn">⇄</span></div>
</div>
<div class="abs product" style="left:874px;top:1571px">
  <div class="img" style="position:relative"><div role="img" aria-label="Pile of colourful novelty sunglasses" style="background:radial-gradient(circle,#4fb7e6 0%,#e88a3a 45%,#fff 72%)"></div></div>
  <h4>At vero eos et accusamus et iust odio dignissimos</h4><div class="price">$69.99</div>
  <div class="actions"><a class="btn-gold">ADD TO CART</a><span class="icon-btn">♥</span><span class="icon-btn">i</span><span class="icon-btn">⇄</span></div>
</div>

<div class="abs product" style="left:99px;top:2000px">
  <div class="img" style="position:relative"><div role="img" aria-label="Green and purple feathered masquerade mask" style="background:radial-gradient(circle,#7fb44a 0%,#8a6cb0 45%,#fff 72%)"></div></div>
  <h4>At vero eos et accusamus et iust odio dignissimos</h4><div class="price">$69.99</div>
  <div class="actions"><a class="btn-gold">ADD TO CART</a><span class="icon-btn">♥</span><span class="icon-btn">i</span><span class="icon-btn">⇄</span></div>
</div>
<div class="abs product" style="left:357px;top:2000px">
  <div class="img" style="position:relative"><div role="img" aria-label="Red heart-shaped sunglasses" style="background:radial-gradient(circle,#e23a3a 0%,#c52a2a 35%,#fff 70%)"></div></div>
  <h4>At vero eos et accusamus et iust odio dignissimos</h4><div class="price">$69.99</div>
  <div class="actions"><a class="btn-gold">ADD TO CART</a><span class="icon-btn">♥</span><span class="icon-btn">i</span><span class="icon-btn">⇄</span></div>
</div>
<div class="abs product" style="left:615px;top:2000px">
  <div class="img" style="position:relative"><div role="img" aria-label="Assorted patterned gift bags" style="background:radial-gradient(circle,#e27aa8 0%,#8a8a8a 45%,#fff 72%)"></div></div>
  <h4>At vero eos et accusamus et iust odio dignissimos</h4><div class="price">$69.99</div>
  <div class="actions"><a class="btn-gold">ADD TO CART</a><span class="icon-btn">♥</span><span class="icon-btn">i</span><span class="icon-btn">⇄</span></div>
</div>
<div class="abs product" style="left:874px;top:2000px">
  <div class="img" style="position:relative"><div role="img" aria-label="Scattered lollipops and candy canes" style="background:radial-gradient(circle,#f0a3c2 0%,#f2c94c 40%,#fff 72%)"></div></div>
  <h4>At vero eos et accusamus et iust odio dignissimos</h4><div class="price">$69.99</div>
  <div class="actions"><a class="btn-gold">ADD TO CART</a><span class="icon-btn">♥</span><span class="icon-btn">i</span><span class="icon-btn">⇄</span></div>
</div>

<div class="abs view-more"><span>VIEW MORE PRODUCTS</span></div>

<section class="abs band">
  <svg class="abs" style="left:48px;top:72px" width="14" height="24"><path d="M12 1L2 12l10 11" fill="none" stroke="#cfe0e4" stroke-width="2"/></svg>
  <svg class="abs" style="left:1138px;top:72px" width="14" height="24"><path d="M2 1l10 11-10 11" fill="none" stroke="#cfe0e4" stroke-width="2"/></svg>
  <div class="abs feature" style="left:99px">
    <svg width="56" height="56" viewBox="0 0 56 56"><rect x="8" y="4" width="40" height="40" rx="6" fill="#fff"/><rect x="13" y="10" width="30" height="14" fill="#7aa3ae"/><circle cx="17" cy="34" r="3" fill="#7aa3ae"/><circle cx="39" cy="34" r="3" fill="#7aa3ae"/><rect x="12" y="44" width="8" height="8" fill="#fff"/><rect x="36" y="44" width="8" height="8" fill="#fff"/></svg>
    <div><b>Free Shipping</b><small>Ducimus qui blanditiis</small></div>
  </div>
  <div class="abs feature" style="left:355px">
    <svg width="46" height="56" viewBox="0 0 46 56"><path d="M11 24V15a12 12 0 0124 0v9" fill="none" stroke="#fff" stroke-width="5"/><rect x="4" y="24" width="38" height="28" rx="3" fill="#fff"/></svg>
    <div><b>100% Secure</b><small>Ducimus qui blanditiis</small></div>
  </div>
  <div class="abs feature" style="left:600px">
    <svg width="66" height="50" viewBox="0 0 66 50"><rect x="9" y="4" width="48" height="32" rx="2" fill="none" stroke="#fff" stroke-width="4"/><rect x="2" y="40" width="62" height="6" rx="2" fill="#fff"/></svg>
    <div><b>Best Online</b><small>Ducimus qui blanditiis</small></div>
  </div>
  <div class="abs feature" style="left:853px">
    <svg width="70" height="56" viewBox="0 0 70 56"><circle cx="35" cy="16" r="10" fill="#fff"/><path d="M17 54a18 18 0 0136 0z" fill="#fff"/><circle cx="14" cy="22" r="7" fill="#fff"/><circle cx="56" cy="22" r="7" fill="#fff"/><path d="M1 48a13 13 0 0120-10v10z" fill="#fff"/><path d="M69 48a13 13 0 00-20-10v10z" fill="#fff"/></svg>
    <div><b>Customer Support</b><small>Ducimus qui blanditiis</small></div>
  </div>
</section>

<div class="abs fcol" style="left:99px">
  <h5>Information</h5>
  <ul><li>About Us</li><li>Careers</li><li>Privacy &amp; Security</li><li>Site Map</li><li>Terms of Use</li><li>Blog</li></ul>
</div>
<div class="abs fsep" style="left:258px"></div>
<div class="abs fcol" style="left:303px">
  <h5>Help &amp; support</h5>
  <ul><li>Recommended Reading</li><li>Submit your Story</li><li>Contact Us</li><li>Frequently Asked Questions</li><li>How to Order</li></ul>
</div>
<div class="abs fsep" style="left:506px"></div>
<div class="abs fcol" style="left:551px">
  <h5>My Account</h5>
  <ul><li>Delivery Information</li><li>My Account</li><li>Order Tracking</li><li>Reminder Service</li><li>Shipping, Returns &amp; Fees</li></ul>
</div>
<div class="abs fsep" style="left:732px"></div>
<div class="abs fcol" style="left:777px;width:324px">
  <h5>Email Subscription</h5>
  <p style="margin-top:-6px">Register your email address to get information about us</p>
  <div class="subscribe"><div class="input">Email Address</div><a class="btn-gold">SUBSCRIBE</a></div>
  <h5 style="margin:16px 0 0">Stay Connected</h5>
  <div class="social"><i></i><i></i><i></i><i></i><i></i><i></i><i></i><i></i></div>
</div>

<div class="abs copyright">Copyrights © 2017, Partyloom. All Rights Reserved &nbsp;|&nbsp; Privacy Policy | Terms of Use | Feedback</div>

</body>
</html>
```